Corvane Edge Supplies - Stone Tooling Company

We need a round design for a saw blade that cuts stone.

We provide the tools and equipment necessary to cut, shape, polish granite-marble-engineered stone for your home.

Think designs on a skateboard wheel. Urban-street designs. We like something along the lines of something similar to the wheels on larkhollowrolls.com, snowboard designs etc..

2 Colors. Background - Matte Black. Gold print on top.
No shading/gradient as this has to be solid colors black/gold.
We would like the following text imbedded somewhere-
"Approved by Tall Morris"
"Granite/Engineered Stone"

Must have logo thats in the file

Target Market(s)

granite countertop fabricators- current designs are boring- we want this to stand out.

Industry/Entity Type

It Company

Font styles to use
Sans Serif
Decorative

Requirements
Must have
• Check attached picture. Something similar except with our attached logo, black background, and gold print.
Nice to have
• urban, street, skate, surf, tattoo, style
Should not have
• shadowing, unless by dots and lines for silk screen printing.

```html
<!DOCTYPE html>
<html lang="en">
<head>
<meta charset="utf-8">
<title>Corvane Edge Supplies — Stone Saw Blade</title>
<link rel="stylesheet" href="https://fonts.googleapis.com/css2?family=Archivo+Black&family=Archivo:wght@700&display=swap">
<style>
  :root {
    --steel-light: #c9c9c9;
    --steel-bright: #f2f2f2;
    --steel-dark: #7d7d7d;
    --slot: #ffffff;
    --matte-black: #000000;
    --gold: #958f12;
    --gold-deep: #7f7a0e;
    --bore: #ffffff;
    --bore-rim: #d6d6d6;
  }
  html, body {
    margin: 0;
    padding: 0;
    width: 1200px;
    height: 1200px;
    overflow: hidden;
    background: #ffffff;
  }
  .blade-canvas {
    display: block;
    width: 1200px;
    height: 1200px;
  }
  .slot { stroke: var(--slot); stroke-width: 7; stroke-linecap: butt; }
  .label-ring { fill: var(--matte-black); }
  .core-gap { fill: none; stroke: var(--steel-light); stroke-width: 9; }
  .brand-name {
    font-family: "Archivo Black", "Arial Black", sans-serif;
    font-size: 84px;
    fill: var(--gold);
  }
  .brand-dot { fill: var(--gold); }
  .material-line {
    font-family: "Archivo", Arial, sans-serif;
    font-weight: 700;
    font-size: 18px;
    fill: var(--gold);
  }
  .approval-line {
    font-family: "Archivo", Arial, sans-serif;
    font-weight: 700;
    font-size: 22px;
    fill: var(--gold);
  }
  .hub-ornament { fill: none; stroke: var(--gold-deep); stroke-width: 118; }
  .arbor-hole { fill: var(--bore); stroke: var(--bore-rim); stroke-width: 6; }
</style>
</head>
<body>
<svg class="blade-canvas" viewBox="0 0 1200 1200" xmlns="http://www.w3.org/2000/svg" xmlns:xlink="http://www.w3.org/1999/xlink">
  <defs>
    <linearGradient id="steel-face" x1="0" y1="0" x2="1" y2="0">
      <stop offset="0" stop-color="var(--steel-light)"/>
      <stop offset="0.55" stop-color="var(--steel-bright)"/>
      <stop offset="1" stop-color="var(--steel-dark)"/>
    </linearGradient>
    <line id="rim-slot" class="slot" x1="600" y1="44" x2="604" y2="118"/>
    <path id="brand-arc" d="M348.9 555.7 A255 255 0 0 1 591.1 345.2"/>
    <path id="material-arc" d="M640.6 310.8 A292 292 0 0 1 891.8 589.8"/>
    <path id="approval-arc" d="M635.9 344.5 A258 258 0 0 1 857.8 591.0"/>
    <g id="label-set">
      <circle class="brand-dot" cx="310" cy="600" r="22"/>
      <text class="brand-name"><textPath xlink:href="#brand-arc" textLength="340" lengthAdjust="spacingAndGlyphs">Corvane</textPath></text>
      <text class="material-line"><textPath xlink:href="#material-arc" textLength="340" lengthAdjust="spacingAndGlyphs">GRANITE &amp; ENGINEERED STONE</textPath></text>
      <text class="approval-line"><textPath xlink:href="#approval-arc" textLength="330" lengthAdjust="spacingAndGlyphs">APPROVED BY TALL MORRIS</textPath></text>
    </g>
  </defs>

  <g class="blade-body">
    <circle cx="600" cy="600" r="556" fill="url(#steel-face)"/>
    <g class="rim-slots">
      <use xlink:href="#rim-slot" transform="rotate(0 600 600)"/>
      <use xlink:href="#rim-slot" transform="rotate(12 600 600)"/>
      <use xlink:href="#rim-slot" transform="rotate(24 600 600)"/>
      <use xlink:href="#rim-slot" transform="rotate(36 600 600)"/>
      <use xlink:href="#rim-slot" transform="rotate(48 600 600)"/>
      <use xlink:href="#rim-slot" transform="rotate(60 600 600)"/>
      <use xlink:href="#rim-slot" transform="rotate(72 600 600)"/>
      <use xlink:href="#rim-slot" transform="rotate(84 600 600)"/>
      <use xlink:href="#rim-slot" transform="rotate(96 600 600)"/>
      <use xlink:href="#rim-slot" transform="rotate(108 600 600)"/>
      <use xlink:href="#rim-slot" transform="rotate(120 600 600)"/>
      <use xlink:href="#rim-slot" transform="rotate(132 600 600)"/>
      <use xlink:href="#rim-slot" transform="rotate(144 600 600)"/>
      <use xlink:href="#rim-slot" transform="rotate(156 600 600)"/>
      <use xlink:href="#rim-slot" transform="rotate(168 600 600)"/>
      <use xlink:href="#rim-slot" transform="rotate(180 600 600)"/>
      <use xlink:href="#rim-slot" transform="rotate(192 600 600)"/>
      <use xlink:href="#rim-slot" transform="rotate(204 600 600)"/>
      <use xlink:href="#rim-slot" transform="rotate(216 600 600)"/>
      <use xlink:href="#rim-slot" transform="rotate(228 600 600)"/>
      <use xlink:href="#rim-slot" transform="rotate(240 600 600)"/>
      <use xlink:href="#rim-slot" transform="rotate(252 600 600)"/>
      <use xlink:href="#rim-slot" transform="rotate(264 600 600)"/>
      <use xlink:href="#rim-slot" transform="rotate(276 600 600)"/>
      <use xlink:href="#rim-slot" transform="rotate(288 600 600)"/>
      <use xlink:href="#rim-slot" transform="rotate(300 600 600)"/>
      <use xlink:href="#rim-slot" transform="rotate(312 600 600)"/>
      <use xlink:href="#rim-slot" transform="rotate(324 600 600)"/>
      <use xlink:href="#rim-slot" transform="rotate(336 600 600)"/>
      <use xlink:href="#rim-slot" transform="rotate(348 600 600)"/>
    </g>
  </g>

  <g class="label-disc">
    <circle class="label-ring" cx="600" cy="600" r="384"/>
    <circle class="core-gap" cx="600" cy="600" r="371"/>
    <g class="hub-ornament-area" role="img" aria-label="Gold spiral of curved blade teeth circling the arbor hole">
      <circle class="hub-ornament" cx="600" cy="600" r="146"/>
    </g>
    <use xlink:href="#label-set"/>
    <use xlink:href="#label-set" transform="rotate(180 600 600)"/>
    <circle class="arbor-hole" cx="600" cy="600" r="84"/>
  </g>
</svg>
</body>
</html>
```